Business Cards and stationary for Home builder
Business Cards and stationary for Home builder - Construction
Professional
Marv T. Osko
Group Box 812 RR # 7 Saskatoon, Sk. S7N 5L2 CANADA
marv@quillforge.ca
quillforge.ca
Big Logo And: Building Saskatchewan since 1986 Hire carpenters to build your home

```html
<!DOCTYPE html>
<html lang="en">
<head>
<meta charset="utf-8">
<title>Quillforge business cards</title>
<link href="https://fonts.googleapis.com/css2?family=Arimo:wght@400;700&display=swap" rel="stylesheet">
<style>
  :root {
    --bg: #8a8f7e;
    --card: #ffffff;
    --green: #1f7f35;
    --green-dark: #145c25;
    --grey-band: #6d6e70;
    --grey-light: #d9dadb;
    --text: #555759;
    --divider: #c9cacb;
  }
  * { margin: 0; padding: 0; box-sizing: border-box; }
  html, body { width: 1200px; height: 852px; overflow: hidden; }
  body { background: var(--bg); font-family: "Arimo", Arial, sans-serif; position: relative; }

  .card {
    position: absolute;
    width: 540px; height: 310px;
    background: var(--card);
    border-radius: 18px;
    overflow: hidden;
    box-shadow: 0 6px 18px rgba(0,0,0,.25);
  }
  .card--front { left: 70px; top: 110px; }
  .card--back { left: 600px; top: 440px; }

  .card__band { position: absolute; left: 0; top: 0; width: 540px; height: 310px; }

  .wordmark {
    position: absolute;
    display: flex; align-items: center;
    color: var(--green);
    font-weight: 700;
    text-transform: uppercase;
    letter-spacing: 0.5px;
    white-space: nowrap;
    line-height: 1;
  }
  .wordmark__mark { background: var(--green); display: block; }
  .card--front .wordmark { left: 40px; top: 72px; font-size: 26px; gap: 9px; }
  .card--front .wordmark__mark { width: 22px; height: 22px; }
  .card--back .wordmark { left: 34px; top: 186px; font-size: 20px; gap: 7px; }
  .card--back .wordmark__mark { width: 15px; height: 15px; }

  .divider { position: absolute; width: 1px; background: var(--divider); }
  .card--front .divider { left: 290px; top: 56px; height: 150px; }
  .card--back .divider { left: 250px; top: 38px; height: 186px; }

  .person { position: absolute; color: var(--text); font-size: 12.5px; line-height: 1.35; }
  .person__name { color: var(--green); font-weight: 700; font-size: 15px; margin-bottom: 5px; }
  .card--front .person { right: 262px; top: 118px; text-align: right; }
  .card--back .person { left: 266px; top: 40px; }

  .contacts { position: absolute; list-style: none; color: var(--text); font-size: 12.5px; }
  .contacts li { display: flex; align-items: center; gap: 7px; height: 19px; }
  .contacts svg { width: 12px; height: 12px; fill: var(--green); flex: none; }
  .card--front .contacts { left: 302px; top: 62px; }
  .card--back .contacts { left: 266px; top: 124px; }
</style>
</head>
<body>

<svg width="0" height="0" style="position:absolute">
  <defs>
    <symbol id="icon-phone" viewBox="0 0 12 12"><path d="M2.5 0.5 L4.5 0.5 L5 3.5 L3.7 4.4 C4.4 6 5.8 7.5 7.5 8.3 L8.5 7 L11.5 7.5 L11.5 9.5 C11.5 10.8 10.5 11.5 9.5 11.5 C4.5 11 1 7.5 0.5 2.5 C0.5 1.4 1.3 0.5 2.5 0.5Z"/></symbol>
    <symbol id="icon-mobile" viewBox="0 0 12 12"><path d="M3 0 H9 A1 1 0 0 1 10 1 V11 A1 1 0 0 1 9 12 H3 A1 1 0 0 1 2 11 V1 A1 1 0 0 1 3 0Z M3.2 1.5 V9.5 H8.8 V1.5Z M6 10 A0.7 0.7 0 1 0 6 11.4 A0.7 0.7 0 1 0 6 10Z"/></symbol>
    <symbol id="icon-fax" viewBox="0 0 12 12"><path d="M3 0 H9 V4 H3Z M1 4.5 H11 A1 1 0 0 1 12 5.5 V10 H9 V12 H3 V10 H0 V5.5 A1 1 0 0 1 1 4.5Z M4 8 V11 H8 V8Z"/></symbol>
    <symbol id="icon-mail" viewBox="0 0 12 12"><path d="M0 2.5 H12 V9.5 H0Z M0.8 3 L6 7 L11.2 3 L11.2 3.6 L6 7.8 L0.8 3.6Z" fill-rule="evenodd"/></symbol>
    <symbol id="icon-web" viewBox="0 0 12 12"><circle cx="6" cy="6" r="5.5"/></symbol>
  </defs>
</svg>

<section class="card card--front">
  <svg class="card__band" viewBox="0 0 540 310" aria-hidden="true">
    <path d="M0 232 C150 218 330 222 540 214 L540 226 C330 236 150 232 0 246Z" fill="var(--grey-light)"/>
    <path d="M0 240 C160 226 340 234 540 222 L540 238 C340 248 170 244 0 256Z" fill="var(--grey-band)"/>
    <path d="M0 254 C170 240 360 250 540 236 L540 310 L0 310Z" fill="var(--green)"/>
    <path d="M0 270 C200 256 380 270 540 252 L540 310 L0 310Z" fill="var(--green-dark)" opacity=".45"/>
  </svg>
  <div class="wordmark"><span class="wordmark__mark"></span>Quillforge</div>
  <div class="divider"></div>
  <div class="person">
    <p class="person__name">Marv T. Osko</p>
    <p>Group Box 812 RR # 7</p>
    <p>Saskatoon, Sk. S7N 5L2</p>
    <p>CANADA</p>
  </div>
  <ul class="contacts">
    <li><svg><use href="#icon-phone"/></svg>306-555-0142</li>
    <li><svg><use href="#icon-mobile"/></svg>306-555-0187</li>
    <li><svg><use href="#icon-fax"/></svg>306-555-0163</li>
    <li><svg><use href="#icon-mail"/></svg>marv@quillforge.ca</li>
    <li><svg><use href="#icon-web"/></svg>www.quillforge.ca</li>
  </ul>
</section>

<section class="card card--back">
  <svg class="card__band" viewBox="0 0 540 310" aria-hidden="true">
    <path d="M0 244 C150 232 330 236 540 228 L540 238 C330 246 150 244 0 256Z" fill="var(--grey-light)"/>
    <path d="M0 250 C160 238 340 244 540 234 L540 248 C340 256 170 254 0 264Z" fill="var(--grey-band)"/>
    <path d="M0 262 C170 250 360 258 540 246 L540 310 L0 310Z" fill="var(--green)"/>
    <path d="M0 278 C200 266 380 278 540 262 L540 310 L0 310Z" fill="var(--green-dark)" opacity=".45"/>
  </svg>
  <div class="divider"></div>
  <div class="person">
    <p class="person__name">Marv T. Osko</p>
    <p>Group Box 812 RR # 7</p>
    <p>Saskatoon, Sk. S7N 5L2</p>
    <p>CANADA</p>
  </div>
  <ul class="contacts">
    <li><svg><use href="#icon-phone"/></svg>306-555-0142</li>
    <li><svg><use href="#icon-mobile"/></svg>306-555-0187</li>
    <li><svg><use href="#icon-fax"/></svg>306-555-0163</li>
    <li><svg><use href="#icon-mail"/></svg>marv@quillforge.ca</li>
    <li><svg><use href="#icon-web"/></svg>www.quillforge.ca</li>
  </ul>
  <div class="wordmark"><span class="wordmark__mark"></span>Quillforge</div>
</section>

</body>
</html>
```